TK Drafting

Simple Design - Logo is done (from this site). Logo on one side - Back Side an image or outline of a house blue print - My name, phone, email, website url. Prefer the traditional Architectural style of letters -

Target Market(s)

Customers who need a floor plan redesigned for renovations or realtors who want a floor plan for marketing their listings

Industry/Entity Type

Architecture

Contact Information for Business Card

Colby Faust - Name
415-362-8840 - Phone
tkdraftingco@mailpost.example
www.tkdraftingco.example

Font styles to use
Other font styles liked:
• Architecture writing -

Colors
0555a3
3276b5
85acd3

Requirements
Must have
• Logo that is attached. I like an indigo blue color for the background or a royal blue - gray logo OR - white and clean with the logo on one side and the same color gray lettering on the other side
Nice to have
• some sort of image that shows a residential blue print. It may not be possible on this small of a card though.
Should not have
• Nothing cartoonish.

```html
<!DOCTYPE html>
<html lang="en">
<head>
<meta charset="utf-8">
<title>TK Drafting – Business Card</title>
<link href="https://fonts.googleapis.com/css2?family=Raleway:wght@400&display=swap" rel="stylesheet">
<style>
  :root {
    --backdrop: #e6e6e6;
    --card: #ffffff;
    --ink: #a9a9b1;
    --ink-light: #b9b9c0;
    --plan-tone: #eeeef3;
    --plan-fade: #f7f7fa;
  }
  * { margin: 0; padding: 0; box-sizing: border-box; }
  html, body {
    width: 1200px;
    height: 707px;
    overflow: hidden;
    background: var(--backdrop);
    font-family: "Raleway", sans-serif;
  }
  .stage { position: relative; width: 1200px; height: 707px; }
  .card {
    position: absolute;
    top: 201px;
    width: 388px;
    height: 242px;
    background: var(--card);
    box-shadow: 0 1px 3px rgba(0,0,0,0.08);
    overflow: hidden;
  }
  .card--front { left: 175px; }
  .card--back { left: 633px; }

  .brand {
    position: absolute;
    inset: 0;
    display: flex;
    align-items: center;
    justify-content: center;
    gap: 12px;
  }
  .brand__mark {
    width: 22px;
    height: 22px;
    background: var(--ink);
  }
  .brand__name {
    font-size: 30px;
    font-weight: 400;
    color: var(--ink);
    letter-spacing: 1px;
  }

  .floor-plan {
    position: absolute;
    inset: 0;
    width: 388px;
    height: 242px;
  }

  .contact {
    position: absolute;
    left: 46px;
    top: 0;
    color: var(--ink);
  }
  .contact__name {
    position: absolute;
    top: 78px;
    white-space: nowrap;
    font-size: 16.5px;
  }
  .contact__phone {
    position: absolute;
    top: 124px;
    white-space: nowrap;
    font-size: 21px;
  }
  .contact__email,
  .contact__web {
    position: absolute;
    white-space: nowrap;
    font-size: 13px;
    color: var(--ink-light);
  }
  .contact__email { top: 158px; }
  .contact__web { top: 177px; }
</style>
</head>
<body>
<main class="stage">
  <section class="card card--front">
    <div class="brand">
      <span class="brand__mark"></span>
      <span class="brand__name">TK Drafting</span>
    </div>
  </section>

  <section class="card card--back">
    <svg class="floor-plan" viewBox="0 0 388 242" role="img" aria-label="Faint residential floor plan outline fading in from the right edge">
      <defs>
        <linearGradient id="planFade" x1="0" y1="0" x2="1" y2="0">
          <stop offset="0" stop-color="var(--plan-fade)"/>
          <stop offset="1" stop-color="var(--plan-tone)"/>
        </linearGradient>
      </defs>
      <polygon points="190,0 388,0 388,242 315,242 165,50" fill="url(#planFade)"/>
    </svg>
    <div class="contact">
      <p class="contact__name">Colby Faust</p>
      <p class="contact__phone">415-362-8840</p>
      <p class="contact__email">tkdraftingco@mailpost.example</p>
      <p class="contact__web">www.tkdraftingco.example</p>
    </div>
  </section>
</main>
</body>
</html>
```